We’re a real estate firm that has landed a big builder in a neighboring state. Our branding needs...

We are a real estate firm who represents various builders along with doing resale here in Oregon. Our firm is growing to represent a big builder in Washington State and we’ll have another 40 brokers on our team. We need rebranding. As in, a new logo ( the house logo we have now looks cartoonish, hate it). We need new cards, something to really stand out. I’ve been thinking of using those NFC cards from ZIB or the ones with the seam color. I likely want two or three designs, a darker (as in a background color of black or grey) , a light one ( again I mean background color) and a credit card style (either plastic w an embossed name/number on front, or metal ). I’m thinking dark background for cc, or silver if it’s metal. That’s my thoughts, but you are the artists, so maybe you have an idea I haven’t considered. Our colors were black and red, but we don’t have to stick to that. Just nothing too busy. Oh, and we are typically representing the local, higher quality builders in our area (just below custom), but not national. Subdivisions are near the Kel Varsby, Tobrin, and Ashfield Coastal sites. We are super excited, but without a lot of time to change the “look” of our brokerage. So I’ll be deciding and moving forward within 24 hours tops. Our name is Real Estate Summitline Partners ( we cant change the name because of timeline and business license) Thank you!

Industry/Entity Type

Real Estate

Contact Information for Business Card

The usual. Name of firm. Name of cardholder. Contact info.

Font styles to use
Serif
Sans Serif

Colors

Designer to choose colors to be used in the design.

Requirements
Must have
• A sleek or simple look. I included photos of cards with stylistic attributes we like. Thank you
Nice to have
• We really like the black backgrounds. With foil or embossed detail. We also like the black on black. Matte black card with raised shiny black detail. But still eye catching.
Should not have
• No ornate or busy looking style. We don’t want anything cluttered.

```html
<!DOCTYPE html>
<html lang="en">
<head>
<meta charset="utf-8">
<title>Real Estate Summitline Partners — Business Card</title>
<link href="https://fonts.googleapis.com/css2?family=Open+Sans:wght@400;700&display=swap" rel="stylesheet">
<style>
  :root {
    --backdrop: #2b2624;
    --card: #0c0c0d;
    --card-edge: #1a1a1b;
    --brand-blue: #1b6fd6;
    --text-grey: #b9b9b9;
    --rule-grey: #555555;
    --silver: #d6d6d6;
  }
  * { box-sizing: border-box; margin: 0; padding: 0; }
  html, body {
    width: 1200px; height: 844px; overflow: hidden;
    background: var(--backdrop);
    font-family: "Open Sans", Arial, sans-serif;
  }
  .canvas {
    position: relative; width: 1200px; height: 844px;
    display: flex; align-items: center; justify-content: center; gap: 60px;
  }
  .card {
    position: relative; width: 510px; height: 292px;
    background: var(--card);
    border: 1px solid var(--card-edge);
    border-radius: 4px;
    box-shadow: 0 18px 40px rgba(0,0,0,.55);
  }
  .wordmark {
    font-family: "Open Sans", Arial, sans-serif;
    font-weight: 700; line-height: 1.05; letter-spacing: .5px;
  }
  .card-front .wordmark {
    position: absolute; left: 44px; top: 34px; width: 320px;
    font-size: 27px; color: var(--brand-blue);
  }
  .card-front .rule {
    position: absolute; left: 44px; top: 110px; width: 270px;
    height: 1px; background: var(--rule-grey);
  }
  .contact {
    position: absolute; right: 30px; top: 132px;
    list-style: none; text-align: right;
  }
  .contact li {
    display: flex; align-items: center; justify-content: flex-end; gap: 6px;
    font-size: 13.5px; line-height: 19px; color: var(--text-grey);
  }
  .contact svg { width: 10px; height: 10px; fill: var(--brand-blue); flex: none; }
  .holder { position: absolute; left: 44px; bottom: 34px; }
  .holder-name { font-size: 17px; font-weight: 700; color: var(--brand-blue); letter-spacing: .3px; }
  .holder-role { font-size: 14px; color: var(--text-grey); margin-bottom: 10px; }
  .holder-address { font-size: 14px; line-height: 18px; color: var(--text-grey); font-style: normal; }
  .card-back { display: flex; align-items: center; justify-content: center; }
  .card-back .wordmark {
    font-size: 30px; color: var(--silver); text-align: center; width: 360px;
  }
</style>
</head>
<body>
<main class="canvas">
  <section class="card card-front" aria-label="Card front">
    <div class="wordmark">Real Estate Summitline Partners</div>
    <div class="rule"></div>
    <ul class="contact">
      <li>503-555-0148
        <svg viewBox="0 0 10 10" aria-hidden="true"><path d="M2 0h2l1 2.5-1.3 1a6 6 0 0 0 2.8 2.8l1-1.3L10 6v2a2 2 0 0 1-2 2A8 8 0 0 1 0 2a2 2 0 0 1 2-2z"/></svg></li>
      <li>503-555-0172
        <svg viewBox="0 0 10 10" aria-hidden="true"><path d="M2.5 0h5a1 1 0 0 1 1 1v8a1 1 0 0 1-1 1h-5a1 1 0 0 1-1-1V1a1 1 0 0 1 1-1zm.5 1.5v6h4v-6z"/></svg></li>
      <li>info@summitline.co
        <svg viewBox="0 0 10 10" aria-hidden="true"><path d="M0 2h10v6H0zm1 1 4 3 4-3z"/></svg></li>
      <li>www.summitline.co
        <svg viewBox="0 0 10 10" aria-hidden="true"><circle cx="5" cy="5" r="5"/></svg></li>
    </ul>
    <div class="holder">
      <p class="holder-name">DANA WHITCOMB</p>
      <p class="holder-role">Managing Director</p>
      <address class="holder-address">2210 Alder Crest Way<br>Portland, OR 97205</address>
    </div>
  </section>
  <section class="card card-back" aria-label="Card back">
    <div class="wordmark">Real Estate Summitline Partners</div>
  </section>
</main>
</body>
</html>
```